R. K. Belvard & Associates, Inc

Gregor Belvard
Accountant
4219 NW 168th ST
Hialeah, Florida 33015
(305) 555-0187
greg.belvard@quillmarsh.com
Accounting - Tax Preparation Services - Bookkeeping
Side - one business logo on the left and business information on right
On Backside: The logo in the middle and under the logo my company name.

Rounded Corner of the cards
In reference to the logo and cards I need to adjust the circle around the RK and color.

```html
<!DOCTYPE html>
<html lang="en">
<head>
<meta charset="utf-8">
<title>R. K. Belvard &amp; Associates, Inc — Business Cards</title>
<link rel="stylesheet" href="https://fonts.googleapis.com/css2?family=Montserrat:wght@500;700&family=Poppins:wght@400;500;600&display=swap">
<style>
  :root {
    --backdrop: #2b2b2d;
    --brand-blue: #0b6fc1;
    --ink: #1b1b1d;
    --paper: #ffffff;
    --muted-ink: #2a2a2a;
  }
  * { box-sizing: border-box; margin: 0; padding: 0; }
  html, body { width: 1200px; height: 1189px; overflow: hidden; }
  body {
    background: var(--backdrop);
    font-family: "Poppins", sans-serif;
    position: relative;
  }
  .card {
    position: absolute;
    left: 150px;
    width: 900px;
    height: 514px;
    border-radius: 34px;
    box-shadow: 0 12px 30px rgba(0,0,0,.45);
    overflow: hidden;
  }
  /* Back side */
  .card-back {
    top: 50px;
    background: var(--brand-blue);
    color: var(--paper);
    display: flex;
    flex-direction: column;
    align-items: center;
    justify-content: center;
  }
  .back-mark {
    font-family: "Poppins", sans-serif;
    font-weight: 600;
    font-size: 130px;
    line-height: 1;
    letter-spacing: 4px;
    color: var(--paper);
  }
  .company-name {
    margin-top: 28px;
    font-family: "Montserrat", sans-serif;
    text-align: center;
    line-height: 1.2;
  }
  .company-name .line-main { display: block; font-weight: 700; font-size: 38px; letter-spacing: 2px; }
  .company-name .line-sub { display: block; font-weight: 500; font-size: 31px; letter-spacing: 2px; }

  /* Front side */
  .card-front {
    top: 620px;
    background: var(--paper);
    color: var(--ink);
  }
  .front-mark {
    position: absolute;
    left: 70px; top: 110px;
    width: 250px; height: 220px;
    display: flex; align-items: center; justify-content: center;
    font-weight: 600;
    font-size: 120px;
    color: var(--ink);
    letter-spacing: 4px;
  }
  .divider {
    position: absolute;
    left: 360px; top: 90px;
    width: 2px; height: 250px;
    background: var(--brand-blue);
  }
  .contact {
    position: absolute;
    left: 410px; top: 92px;
  }
  .person-name { font-weight: 600; font-size: 34px; line-height: 1.05; color: var(--ink); }
  .person-role { font-weight: 500; font-size: 22px; color: var(--brand-blue); margin-bottom: 20px; }
  .address { font-size: 21px; line-height: 1.35; color: var(--muted-ink); margin-bottom: 22px; }
  .contact-line { display: flex; align-items: center; gap: 12px; font-size: 21px; line-height: 1.5; color: var(--muted-ink); }
  .contact-icon { width: 26px; height: 26px; flex: none; }
  .services {
    position: absolute;
    left: 0; right: 0; bottom: 58px;
    text-align: center;
    font-size: 25px;
    letter-spacing: .5px;
    color: var(--muted-ink);
  }
  .services .sep { color: var(--brand-blue); margin: 0 10px; font-weight: 500; }
</style>
</head>
<body>
  <section class="card card-back" aria-label="Card back">
    <div class="back-mark">RK</div>
    <h1 class="company-name">
      <span class="line-main">R. K. BELVARD &amp;</span>
      <span class="line-sub">ASSOCIATES, INC</span>
    </h1>
  </section>

  <section class="card card-front" aria-label="Card front">
    <div class="front-mark">RK</div>
    <div class="divider"></div>
    <div class="contact">
      <h2 class="person-name">Gregor Belvard</h2>
      <p class="person-role">Accountant</p>
      <p class="address">4219 NW 168th ST<br>Hialeah, Florida 33015</p>
      <p class="contact-line">
        <svg class="contact-icon" viewBox="0 0 26 26" aria-hidden="true">
          <circle cx="13" cy="13" r="13" fill="var(--brand-blue)"/>
          <path d="M9 7.5c.6-.5 1.3-.4 1.7.2l1.1 1.8c.3.5.2 1.1-.2 1.4l-.8.6c.6 1.4 1.6 2.5 3 3.1l.6-.8c.4-.4 1-.5 1.4-.2l1.8 1.1c.6.4.7 1.2.2 1.7l-.9.9c-.8.8-2 .9-3 .4-2.7-1.3-4.7-3.3-6-6-.5-1-.4-2.2.4-3z" fill="#fff"/>
        </svg>
        (305) 555-0187
      </p>
      <p class="contact-line">
        <svg class="contact-icon" viewBox="0 0 26 26" aria-hidden="true">
          <circle cx="13" cy="13" r="13" fill="var(--brand-blue)"/>
          <rect x="7" y="8.5" width="12" height="9" rx="1" fill="none" stroke="#fff" stroke-width="1.5"/>
          <path d="M7.5 9l5.5 4.5L18.5 9" fill="none" stroke="#fff" stroke-width="1.5"/>
        </svg>
        greg.belvard@quillmarsh.com
      </p>
    </div>
    <p class="services">Accounting<span class="sep">|</span>Tax Preparation Services<span class="sep">|</span>Bookkeeping</p>
  </section>
</body>
</html>
```